Quartz Meridian Business Card Design

I need a 2-sided business card for my computer engineering consulting company. The card is expected to convey a message of cutting edge forward thinking, and boldnes. I would like the card to be memorable and stand-out on a desk. The card should be bold, modern, clean, and highly professional. I am a big fan of watermarks/shadows and other intersting but restrained uses of the logo. The card can be a shape other than the traditional rectangle. Perhaps a rectangle with rounded edges. All I ask is the card be able to fit into a standard wallet. I will supply two logos, one with a red background, and one with a black background. Please feel free to work with both of these logos.
Updates

Hi all, thank you for your submissions. I will post the original vector file later today. Thank you for your patience.

Regards,

Henry

Target Market(s)

Engineering Buyers, Vice Presidents and Directors

Industry/Entity Type

Computer

Requirements
Must have
• 2 sides

```html
<!DOCTYPE html>
<html lang="en">
<head>
<meta charset="utf-8">
<title>Quartz Meridian Business Card</title>
<link href="https://fonts.googleapis.com/css2?family=Open+Sans:wght@400;600;700&display=swap" rel="stylesheet">
<style>
  :root {
    --backdrop: #ece9e4;
    --card-black: #000000;
    --card-grey: #565656;
    --brand-red: #c1272d;
    --text-white: #ffffff;
    --text-muted: #9a9a9a;
    --divider: #d0202a;
  }
  * { margin: 0; padding: 0; box-sizing: border-box; }
  html, body {
    width: 1200px; height: 473px; overflow: hidden;
    background: var(--backdrop);
    font-family: "Open Sans", Arial, sans-serif;
  }
  .canvas { position: relative; width: 1200px; height: 473px; }
  .card {
    position: absolute; top: 83px; width: 526px; height: 299px;
    border-radius: 14px; overflow: hidden;
    background: var(--card-black);
    box-shadow: 0 4px 10px rgba(0,0,0,0.35);
  }
  .card--front { left: 44px; }
  .card--back { left: 610px; }
  .card__lower {
    position: absolute; left: 0; right: 0; top: 199px; bottom: 0;
    background: var(--card-grey);
    border-top: 2px solid var(--divider);
  }
  .brand-square {
    position: absolute; left: 218px; top: 42px; width: 28px; height: 28px;
    background: var(--brand-red);
  }
  .brand-name {
    position: absolute; left: 0; right: 0; top: 131px;
    text-align: center; color: var(--brand-red);
    font-weight: 700; font-size: 27px; letter-spacing: 0.5px;
    text-transform: uppercase;
  }
  .tagline {
    position: absolute; left: 0; right: 0; top: 165px;
    text-align: center; color: var(--text-muted);
    font-weight: 600; font-size: 14px; letter-spacing: 2.4px;
    text-transform: uppercase;
  }
  .contact {
    position: absolute; left: 0; right: 0; top: 9px;
    text-align: center; color: var(--text-white);
  }
  .contact__name { font-size: 16px; text-transform: uppercase; }
  .contact__title { font-size: 13px; text-transform: none; }
  .contact__line { font-size: 13.5px; margin-top: 6px; }
  .contact__address { font-size: 13.5px; margin-top: 4px; }
  .sep { margin: 0 5px; }
  .website {
    position: absolute; right: 40px; top: 61px;
    color: var(--text-white); font-size: 13px; letter-spacing: 2.4px;
  }
  .back-mark {
    position: absolute; left: 58px; top: 140px;
    display: flex; align-items: center; gap: 12px;
  }
  .back-mark__square { width: 34px; height: 34px; background: var(--brand-red); }
  .back-mark__name {
    color: var(--brand-red); font-weight: 700; font-size: 30px;
    text-transform: uppercase; letter-spacing: 0.5px;
  }
</style>
</head>
<body>
<div class="canvas">
  <section class="card card--front">
    <div class="brand-square"></div>
    <div class="brand-name">Quartz Meridian Works Ltd</div>
    <div class="tagline">Thinking Beyond the Edge</div>
    <div class="card__lower">
      <div class="contact">
        <div class="contact__name">Your Name <span class="contact__title">Title</span></div>
        <div class="contact__line">+91 12345 67890 <span class="sep">|</span> +91 12345 67890 <span class="sep">|</span> info@quartzmeridian.com</div>
        <div class="contact__address">Complex Name, Street&nbsp; City Name,000 000</div>
      </div>
    </div>
  </section>

  <section class="card card--back">
    <div class="card__lower"></div>
    <div class="website">www.quartzmeridian.com</div>
    <div class="back-mark">
      <div class="back-mark__square"></div>
      <div class="back-mark__name">Quartz Meridian</div>
    </div>
  </section>
</div>
</body>
</html>
```